Save The Date for 2019 QRP Symposium

We have an annual meeting each June and need a Save the Date (STD) designed. It should be a two-sided postcard with room for address and stamp (according to US Mail postal standards). I have attached some examples from prior years, but we would appreciate a more modern and attractive design for this year's STD.

Target Market(s)

Our own members - nurses, nurse practitioners, PAs and physicians

Industry/Entity Type

Medical

Requirements
Must have
• Must include our logos (attached), ideally in a coordinating fashion - as was done in prior years (see examples attached) and without modifying the logos too much. Needs have the following information:
• - "Save the Date"
• - "The 12th Annual Vascular Crew Roundtable"
• - "Friday, June 7, 2019" or "6/7/19"
• - "The Halvern–Trask Building | 274 West 19th Street | NYC"
• - Please include our website (www.zq-olm.example/events), phone number (212-555-0147) and email address (ask@zq-olm.example) for people to ask questions
• - Must have space for a postage stamp and the name/address of the postcard recipient
Nice to have
• Would be nice to remain in our blue/grey/olive color palate (see attached Brand Standards guide).
Should not have
• Please do not use stock photos of medical staff. Please don't use cartoons or cartoon images (although a tasteful sketch may be considered).

```html
<!DOCTYPE html>
<html lang="en">
<head>
<meta charset="utf-8">
<title>Save the Date – 12th Annual Vascular Crew Roundtable</title>
<link rel="stylesheet" href="https://fonts.googleapis.com/css2?family=EB+Garamond:ital,wght@0,400;0,600;0,700;1,400&display=swap">
<style>
  :root {
    --backdrop: #bcbec0;
    --card: #ffffff;
    --panel: #bdd4e7;
    --navy: #1b3160;
    --sketch: #5b9fd1;
    --sketch-light: #a9c9e6;
    --veil: rgba(255,255,255,0.55);
  }
  * { box-sizing: border-box; margin: 0; padding: 0; }
  html, body { width: 835px; height: 1200px; overflow: hidden; }
  body {
    background: var(--backdrop);
    font-family: "EB Garamond", Georgia, serif;
    color: var(--navy);
    position: relative;
  }
  .postcard {
    position: absolute;
    left: 111px;
    width: 609px;
    height: 435px;
    background: var(--card);
  }
  .postcard--front { top: 105px; }
  .postcard--back { top: 656px; }
  .panel {
    position: absolute;
    left: 22px; top: 22px; right: 22px; bottom: 22px;
    background: var(--panel);
  }
  .abs { position: absolute; }

  /* front */
  .event-date {
    left: 17px; top: 16px;
    font-weight: 600; font-size: 18px; line-height: 1;
    text-align: center; width: 22px;
  }
  .event-date span { display: block; padding: 3px 0 4px; }
  .event-date span + span { border-top: 1.5px solid var(--navy); }
  .front-sketch {
    left: 165px; top: 10px; width: 201px; height: 294px;
    background: radial-gradient(ellipse at 50% 65%, var(--sketch-light) 0%, rgba(91,159,209,0.35) 55%, rgba(189,212,231,0) 75%);
    border-radius: 40% 40% 50% 50%;
  }
  .venue {
    left: 0; right: 0; text-align: center; font-size: 13.5px;
  }
  .venue--name { top: 131px; }
  .venue--street { top: 191px; }
  .headline {
    left: 0; right: 0; top: 150px;
    text-align: center; font-weight: 700; font-size: 41px;
    letter-spacing: 12px; line-height: 1;
  }
  .headline small {
    font-size: 12px; letter-spacing: 3px; vertical-align: middle;
    margin: 0 18px 0 8px;
  }
  .event-title {
    left: 25px; top: 311px; width: 465px;
    text-align: center; font-size: 22px; line-height: 1.2;
    border-bottom: 1.5px solid var(--navy); padding-bottom: 1px;
  }
  .host { top: 354px; display: flex; align-items: center; gap: 14px; }
  .host-mark {
    width: 35px; height: 35px; border-radius: 50%;
    border: 1.5px solid var(--navy); flex: none;
  }
  .host-mark--solid { background: var(--navy); }
  .host-text { font-size: 8.5px; line-height: 1.3; }
  .host-text em { display: block; }
  .host--society { left: 10px; }
  .host--chapter { left: 226px; }
  .host--center { left: 390px; }
  .contact-line {
    right: 22px; top: 419px;
    font-size: 7.5px; font-style: italic;
  }

  /* back */
  .back-sketch {
    left: 4px; top: 2px; width: 280px; height: 374px;
    background: radial-gradient(ellipse at 55% 60%, var(--sketch-light) 0%, rgba(91,159,209,0.3) 60%, rgba(189,212,231,0) 78%);
    border-radius: 40% 40% 50% 50%;
  }
  .message-area {
    left: 32px; top: 39px; width: 266px; height: 318px;
    background: var(--veil);
  }
  .return-address { left: 351px; top: 38px; display: flex; align-items: flex-start; gap: 5px; }
  .return-mark { width: 29px; height: 29px; border-radius: 50%; background: var(--navy); }
  .return-text { border-left: 1px solid var(--navy); padding-left: 5px; }
  .return-name { font-size: 11px; line-height: 1.1; }
  .return-sub { font-size: 4.5px; line-height: 1.35; }
  .return-sub strong { letter-spacing: 0.4px; }
  .stamp-box {
    left: 492px; top: 19px; width: 53px; height: 57px; background: var(--card);
  }
  .address-line {
    left: 371px; width: 174px; height: 28px; background: var(--card);
  }
  .address-line--1 { top: 150px; }
  .address-line--2 { top: 184px; }
  .address-line--3 { top: 219px; }
</style>
</head>
<body>

<section class="postcard postcard--front">
  <div class="panel">
    <div class="abs front-sketch" role="img" aria-label="Blue pen sketch of a torch-bearing statue rising from an anatomical heart"></div>
    <div class="abs event-date"><span>06</span><span>07</span><span>19</span></div>
    <p class="abs venue venue--name">The Halvern–Trask Building</p>
    <h1 class="abs headline">SAVE <small>THE</small>DATE</h1>
    <p class="abs venue venue--street">274 West 19th Street, NYC</p>
    <h2 class="abs event-title">The 12th Annual Vascular Crew Roundtable</h2>

    <div class="abs host host--society">
      <div class="host-mark"></div>
      <p class="host-text"><em>Presented by</em>The Eastbrook<br>Vascular Society, Inc.</p>
    </div>
    <div class="abs host host--chapter">
      <div class="host-mark host-mark--solid"></div>
      <p class="host-text"><em>of the</em>Northfield State Chapter,<br>Allied College of Vascular Care</p>
    </div>
    <div class="abs host host--center">
      <div class="host-mark"></div>
      <p class="host-text"><em>In association with</em>Eastbrook Heart Center</p>
    </div>
  </div>
  <p class="abs contact-line">For additional information call 212.555.0147 or email ask@zq-olm.example</p>
</section>

<section class="postcard postcard--back">
  <div class="panel">
    <div class="abs back-sketch" role="img" aria-label="Faded blue sketch of a torch-bearing statue rising from an anatomical heart"></div>
    <div class="abs message-area"></div>
    <div class="abs return-address">
      <div class="return-mark"></div>
      <div class="return-text">
        <p class="return-name">Northfield State</p>
        <p class="return-sub"><strong>CHAPTER</strong><br>88 Orchard Lane, Ste. 410<br>New York, NY 10099</p>
      </div>
    </div>
    <div class="abs stamp-box"></div>
    <div class="abs address-line address-line--1"></div>
    <div class="abs address-line address-line--2"></div>
    <div class="abs address-line address-line--3"></div>
  </div>
</section>

</body>
</html>
```